Varolta Business Card

I am looking for a business card design for a start-up company called Varolta Group. This is a management consultancy focused on sales, marketing, sales management, product management and AGILE software development. Our primary customers are $1M to $50M in revenue.

Varolta is the Italian word for "slope."

The path from $0 to $50M has many different growth stages associated with it. Each one having a significant slope to the next plateau. Our expertise helps our customers ascend each of those slopes. We bring experience, successful track-records in growing companies, best practices and a dive-in and roll-up your sleeves mentality. We are not sitting at base camp shouting instructions, we are right there with you, on the climb.

Industry/Entity Type

Business

```html
<!DOCTYPE html>
<html lang="en">
<head>
<meta charset="utf-8">
<title>Varolta Business Card</title>
<link rel="stylesheet" href="https://fonts.googleapis.com/css2?family=Arimo:wght@400&display=swap">
<style>
  :root {
    --page-bg: #e4e4e2;
    --card-bg: #f5f5f4;
    --ink-grey: #5d6770;
    --brand-blue: #0f6cb0;
    --band-blue: #0a5c9e;
    --brand-green: #6aa533;
    --white: #ffffff;
  }
  * { box-sizing: border-box; margin: 0; padding: 0; }
  html, body {
    width: 1200px;
    height: 900px;
    overflow: hidden;
    background: var(--page-bg);
    font-family: "Arimo", Arial, sans-serif;
    color: var(--ink-grey);
  }
  .canvas {
    width: 1200px;
    height: 900px;
    display: flex;
    flex-direction: column;
    align-items: center;
    justify-content: center;
    gap: 50px;
  }
  .card {
    position: relative;
    width: 640px;
    height: 366px;
    background: var(--card-bg);
    box-shadow: 0 2px 10px rgba(0, 0, 0, 0.12);
    overflow: hidden;
  }

  /* Front side */
  .card-front .brand {
    position: absolute;
    left: 90px;
    top: 128px;
    display: flex;
    align-items: center;
    gap: 22px;
  }
  .brand-dot {
    width: 46px;
    height: 46px;
    border-radius: 50%;
    background: var(--brand-blue);
  }
  .brand-name {
    font-weight: 400;
    color: var(--ink-grey);
    letter-spacing: -0.5px;
  }
  .card-front .brand-name { font-size: 76px; }
  .front-stripe {
    position: absolute;
    top: 0;
    bottom: 0;
    left: 474px;
    width: 14px;
    background: var(--brand-green);
  }
  .front-band {
    position: absolute;
    top: 0;
    bottom: 0;
    left: 496px;
    right: 0;
    background: var(--band-blue);
    display: flex;
    align-items: center;
    justify-content: center;
  }
  .front-band .web {
    writing-mode: vertical-rl;
    transform: rotate(180deg);
    color: var(--white);
    font-size: 19px;
    letter-spacing: 0.5px;
  }

  /* Back side */
  .card-back { padding: 38px 44px; }
  .card-back .brand {
    display: flex;
    align-items: center;
    gap: 14px;
  }
  .card-back .brand-dot { width: 30px; height: 30px; }
  .card-back .brand-name { font-size: 42px; }
  .person { margin-top: 26px; }
  .person-name {
    font-size: 24px;
    text-transform: uppercase;
    letter-spacing: 0.3px;
  }
  .person-title { font-size: 14px; margin-top: 3px; }
  .divider {
    width: 380px;
    height: 1.5px;
    background: var(--brand-blue);
    margin: 12px 0 16px;
  }
  .contact {
    display: grid;
    grid-template-columns: 82px auto;
    row-gap: 2px;
    font-size: 14px;
    line-height: 18px;
  }
  .contact dt { color: var(--brand-blue); }
  .contact dd { color: var(--ink-grey); }
  .address {
    font-style: normal;
    font-size: 14px;
    line-height: 18px;
    margin: 12px 0 0 82px;
  }
  .back-web {
    margin: 10px 0 0 82px;
    font-size: 15px;
    color: var(--brand-blue);
  }
</style>
</head>
<body>
  <main class="canvas">
    <section class="card card-front" aria-label="Card front">
      <div class="brand">
        <span class="brand-dot" aria-hidden="true"></span>
        <span class="brand-name">Varolta</span>
      </div>
      <div class="front-stripe"></div>
      <div class="front-band"><span class="web">www.varolta.com</span></div>
    </section>

    <section class="card card-back" aria-label="Card back">
      <div class="brand">
        <span class="brand-dot" aria-hidden="true"></span>
        <span class="brand-name">Varolta</span>
      </div>
      <div class="person">
        <p class="person-name">Daniel Moreau</p>
        <p class="person-title">Product Marketing Manager</p>
      </div>
      <div class="divider"></div>
      <dl class="contact">
        <dt>phone</dt><dd>555.201.4417</dd>
        <dt>fax</dt><dd>555.201.4418</dd>
        <dt>email</dt><dd>daniel@varolta.com</dd>
      </dl>
      <address class="address">2200 Ridgeview Lane, Suite 410,<br>Easton, MA 02356</address>
      <p class="back-web">www.varolta.com</p>
    </section>
  </main>
</body>
</html>
```